The Wellness Barn Business Card

Info for the front..... (in whichever order and layout looks best)
Carla Penhallow
Physiotherapist
4/37 Upper Creekbank Rd
Tallowbrook
QLD 4712
0462305178
carlapenhallow57@mailbox.example
www.thewellnessbarn.example.au
on the back I would like to be able to write appointments so probably just that heading with lines.
I like a sort of rustic style but mostly professional, colours in naturals, beige, brown, green etc. I dont mind if the logo colour is changed slightly to suit.

```html
<!DOCTYPE html>
<html lang="en">
<head>
<meta charset="utf-8">
<title>The Wellness Barn Business Card</title>
<link href="https://fonts.googleapis.com/css2?family=Montserrat:wght@400;700;800&display=swap" rel="stylesheet">
<style>
  :root {
    --olive: #36452a;
    --ink: #6a6a6a;
    --paper: #ffffff;
    --backdrop: #e9eae8;
    --ghost: #f3f3f3;
    --rule: #8a8a8a;
  }
  * { box-sizing: border-box; margin: 0; padding: 0; }
  html, body { width: 1200px; height: 900px; overflow: hidden; }
  body {
    background: var(--backdrop);
    font-family: "Montserrat", sans-serif;
    display: flex;
    flex-direction: column;
    align-items: center;
    justify-content: center;
    gap: 32px;
  }
  .card {
    position: relative;
    width: 720px;
    height: 412px;
    background: var(--paper);
    overflow: hidden;
    box-shadow: 0 2px 10px rgba(0,0,0,0.08);
  }
  .brand-name {
    color: var(--olive);
    font-weight: 800;
    line-height: 1.02;
    text-transform: uppercase;
    letter-spacing: 0.5px;
  }

  /* Appointment side */
  .appointment .brand-name {
    position: absolute;
    top: 54px;
    left: 0; right: 0;
    text-align: center;
    font-size: 34px;
  }
  .appointment-fields {
    position: absolute;
    left: 60px; right: 60px;
    bottom: 70px;
    display: flex;
    flex-direction: column;
    gap: 38px;
    color: var(--ink);
    font-size: 17px;
    letter-spacing: 1px;
  }
  .field-row { display: flex; align-items: flex-end; gap: 10px; }
  .field-line {
    flex: 1;
    border-bottom: 1.5px dashed var(--rule);
    height: 1px;
    margin-bottom: 4px;
  }
  .field-line.short { flex: 0.9; }
  .field-label { white-space: nowrap; }

  /* Contact side */
  .accent-bar {
    position: absolute;
    top: 40px; right: 0;
    width: 30px; height: 44px;
    background: var(--olive);
  }
  .person {
    position: absolute;
    top: 42px; right: 48px;
    text-align: right;
  }
  .person-name {
    color: var(--olive);
    font-weight: 700;
    font-size: 25px;
    letter-spacing: 1.5px;
    text-transform: uppercase;
  }
  .person-role {
    color: var(--ink);
    font-size: 17px;
    letter-spacing: 1px;
    margin-top: 4px;
  }
  .ghost-name {
    position: absolute;
    right: -40px; bottom: 70px;
    color: var(--ghost);
    font-weight: 800;
    font-size: 72px;
    line-height: 0.95;
    text-transform: uppercase;
    text-align: right;
  }
  .contact .brand-name {
    position: absolute;
    top: 142px; left: 52px;
    font-size: 30px;
  }
  .details {
    position: absolute;
    left: 52px; bottom: 34px;
    color: var(--ink);
    font-size: 15px;
    letter-spacing: 0.6px;
    line-height: 1.45;
  }
  .address { margin-bottom: 10px; }
  .contact-line { display: flex; align-items: center; gap: 10px; }
  .contact-line svg { width: 14px; height: 14px; fill: var(--olive); flex: none; }
</style>
</head>
<body>

  <section class="card appointment">
    <div class="brand-name">The Wellness<br>Barn</div>
    <div class="appointment-fields">
      <div class="field-row">
        <span class="field-label">Name :</span>
        <span class="field-line"></span>
      </div>
      <div class="field-row">
        <span class="field-label">Date :</span>
        <span class="field-line short"></span>
        <span class="field-label">Time :</span>
        <span class="field-line short"></span>
        <span class="field-label">am/pm</span>
      </div>
    </div>
  </section>

  <section class="card contact">
    <div class="ghost-name" aria-hidden="true">The Wellness<br>Barn</div>
    <div class="accent-bar"></div>
    <div class="person">
      <div class="person-name">Carla Penhallow</div>
      <div class="person-role">Physiotherapist</div>
    </div>
    <div class="brand-name">The Wellness<br>Barn</div>
    <div class="details">
      <div class="address">4/37 Upper Creekbank Rd<br>Tallowbrook QLD 4712</div>
      <div class="contact-line">
        <svg viewBox="0 0 16 16" aria-hidden="true"><path d="M4 0h8a1 1 0 0 1 1 1v14a1 1 0 0 1-1 1H4a1 1 0 0 1-1-1V1a1 1 0 0 1 1-1zm0 2v10h8V2zm4 11a1 1 0 1 0 0 2 1 1 0 0 0 0-2z"/></svg>
        <span>0462305178</span>
      </div>
      <div class="contact-line">
        <svg viewBox="0 0 16 16" aria-hidden="true"><path d="M0 3h16v10H0zm1.5 1.2V12h13V4.2L8 9z"/></svg>
        <span>carlapenhallow57@mailbox.example</span>
      </div>
      <div class="contact-line">
        <svg viewBox="0 0 16 16" aria-hidden="true"><circle cx="8" cy="8" r="7.5"/><path d="M3 5c2 0 3 1 3 3s2 2 2 4M10 2c0 2 2 2 3 4" stroke="#fff" stroke-width="1.2" fill="none"/></svg>
        <span>www.thewellnessbarn.example.au</span>
      </div>
    </div>
  </section>

</body>
</html>
```